Request for Business Card Design

Hi. My name is Marlena, I am looking for a new business card design for my company, Quillbrook Sensing Systems, LLC. I really like the design you did for Tavel Harvest and was hoping you could do something similar using our full logo and our mark. I am also open to any raised texture design using our mark. I have attached our full logo, which would need to be somewhere on the card, as well as the mark in both outline and full form, as well as our brand colors / guide. The card does not have to be white, as long as our logo and mark appear. I actually like darker colored business cards more, but am open to all options. If you are interested in working with me, please let me know. We would also take the business card design into letterhead design if you can do that.

```html
<!DOCTYPE html>
<html lang="en">
<head>
<meta charset="utf-8">
<title>Quillbrook Sensing Systems – Business Card</title>
<link rel="stylesheet" href="https://fonts.googleapis.com/css2?family=Lato:wght@400;700;900&display=swap">
<style>
  :root {
    --backdrop: #2c2c2e;
    --card: #1e1e20;
    --card-edge: #161618;
    --brand-blue: #1196c6;
    --silver: #c9c9cc;
    --muted: #8a8a8e;
    --text: #d8d8da;
  }
  * { margin: 0; padding: 0; box-sizing: border-box; }
  html, body {
    width: 1200px; height: 799px; overflow: hidden;
    background: var(--backdrop);
    font-family: "Lato", sans-serif;
  }
  .stage {
    position: relative; width: 1200px; height: 799px;
    display: flex; align-items: center; justify-content: center; gap: 48px;
  }
  .card {
    width: 500px; height: 286px;
    background: var(--card);
    border: 1px solid var(--card-edge);
    box-shadow: 0 18px 40px rgba(0,0,0,0.45);
    position: relative;
  }
  /* Front */
  .card--front {
    display: flex; align-items: center; justify-content: center; gap: 18px;
  }
  .brand-dot {
    width: 46px; height: 46px; border-radius: 50%;
    background: var(--brand-blue); flex: none;
  }
  .brand-name {
    color: var(--silver);
    font-weight: 900; font-size: 25px; letter-spacing: 2px;
    text-transform: uppercase; line-height: 1.15;
  }
  /* Back */
  .card--back { display: flex; align-items: center; padding: 0 34px 0 40px; }
  .mark-circle { flex: none; width: 150px; height: 150px; }
  .divider {
    width: 1px; height: 150px; background: var(--brand-blue);
    margin: 0 22px 0 34px; flex: none;
  }
  .contact { color: var(--text); font-size: 12.5px; line-height: 1.45; }
  .contact__name {
    color: var(--brand-blue); font-weight: 900; font-size: 21px;
    letter-spacing: 0.5px; text-transform: uppercase; line-height: 1.1;
  }
  .contact__role { color: var(--muted); font-size: 13px; margin-bottom: 8px; }
  .contact__row { display: flex; align-items: flex-start; gap: 7px; }
  .contact__row svg { width: 10px; height: 10px; margin-top: 4px; flex: none; fill: var(--brand-blue); }
</style>
</head>
<body>
<main class="stage">
  <section class="card card--front" aria-label="Card front">
    <span class="brand-dot" aria-hidden="true"></span>
    <span class="brand-name">Quillbrook<br>Sensing Systems</span>
  </section>

  <section class="card card--back" aria-label="Card back">
    <svg class="mark-circle" viewBox="0 0 150 150" aria-hidden="true">
      <circle cx="75" cy="75" r="70" fill="none" stroke="var(--silver)" stroke-width="2"/>
    </svg>
    <span class="divider" aria-hidden="true"></span>
    <div class="contact">
      <div class="contact__name">Daniel Reyes</div>
      <div class="contact__role">Founder &amp; CEO</div>
      <div class="contact__row">
        <svg viewBox="0 0 10 10"><path d="M5 0a3.5 3.5 0 0 0-3.5 3.5C1.5 6 5 10 5 10s3.5-4 3.5-6.5A3.5 3.5 0 0 0 5 0zm0 5a1.5 1.5 0 1 1 0-3 1.5 1.5 0 0 1 0 3z"/></svg>
        <span>1180 Harbor Point Drive<br>Alder Falls, CO 80911</span>
      </div>
      <div class="contact__row">
        <svg viewBox="0 0 10 10"><path d="M2 0h2l1 2.5-1.3 1a5.5 5.5 0 0 0 2.8 2.8l1-1.3L10 6v2a2 2 0 0 1-2 2A8 8 0 0 1 0 2a2 2 0 0 1 2-2z"/></svg>
        <span>+001 555 210 4471</span>
      </div>
      <div class="contact__row">
        <svg viewBox="0 0 10 10"><path d="M2.5 0h5v3h-5zM0 3.5h10V8H8v2H2V8H0zM3 6.5v2.5h4V6.5z"/></svg>
        <span>+001 555 210 4480</span>
      </div>
      <div class="contact__row">
        <svg viewBox="0 0 10 10"><path d="M0 1.5h10v7H0zM0.8 2.2 5 5.5l4.2-3.3z" fill-rule="evenodd"/></svg>
        <span>marlena@quillbrooksensing.com</span>
      </div>
      <div class="contact__row">
        <svg viewBox="0 0 10 10"><circle cx="5" cy="5" r="4.3" fill="none" stroke="var(--brand-blue)" stroke-width="1.2"/><path d="M0.7 5h8.6M5 0.7c-2.4 2.6-2.4 6 0 8.6M5 0.7c2.4 2.6 2.4 6 0 8.6" fill="none" stroke="var(--brand-blue)" stroke-width="0.9"/></svg>
        <span>quillbrooksensing.com</span>
      </div>
    </div>
  </section>
</main>
</body>
</html>
```